Professional & Modern Technology Business Card

We need a business card for our software/technology firm. Our services include Program/Project Management, Project Controls and Enterprise Analytics. Our clients are usually in the Aviation, Public Works, Transportation and Electric & Water Utility industries. We serve both public and private clients. Would like a very professional, conservative but somewhat modern design. Design, Develop, Deploy is the corporate tagline. We have two offices. The headquarters is in Atlanta, GA and a satellite office In Savannah, GA. Corporate Logo Attached.
Looking to do website and corporate brochure after the successful completion of this project. Would like to begin a working relationship with best designers.
Tagline: Design, Develop, Deploy
Website: www.quambelsystems.example
My Name: Delia Marchetti
My Title: CEO
Email: dmarchetti@quambelsystems.example
Atlanta Address:
87 Corliss Avenue, #2260
Atlanta, GA 30301
Office: 404.555.0178
Fax: 404.555.0143
Mobile: 404.555.0116
Savannah Address:
315 West Harrow Lane Street
Suite 720
Savannah, GA 31401
Office: 912.555.0162
Fax: 404.555.0143
Mobile: 404.555.0116
Please include the email address in your designs: dmarchetti@quambelsystems.example.
I appreciate everyone's design efforts. Just a few notes:
1. Please remove the mobile number from the cards
2. The backs of the cards can be utilized for writing notes. Make sure your design on the back of the card is conducive to clearly adding writing if needed.
3. No black backgrounds please
4. Only use the corporate logo on the front of the card. You can use portions of the logo design, but not the logo in totality.
Thank You
Conservative

```html
<!DOCTYPE html>
<html lang="en">
<head>
<meta charset="utf-8">
<title>Quambel Systems, Inc. – Business Card</title>
<link href="https://fonts.googleapis.com/css2?family=Roboto:wght@300;400;500;700&display=swap" rel="stylesheet">
<style>
  :root {
    --page-bg: #ffffff;
    --card-white: #ffffff;
    --card-back: #f6f6f4;
    --card-border: #e2e2e2;
    --ink: #1a1a1a;
    --ink-soft: #3b3b3b;
    --band: #0b0b0b;
    --band-text: #ffffff;
    --accent-yellow: #f3c300;
    --accent-green: #8cc63f;
    --accent-blue: #27a3dd;
    --web-grey: #6f7173;
    --card-shadow: rgba(0,0,0,0.16);
  }
  * { box-sizing: border-box; margin: 0; padding: 0; }
  html, body {
    width: 1200px; height: 900px; overflow: hidden;
    background: var(--page-bg);
    font-family: "Roboto", Arial, sans-serif;
  }
  .stage {
    position: relative; width: 1200px; height: 900px;
    display: flex; align-items: center; justify-content: center; gap: 44px;
  }
  .card {
    position: relative; width: 530px; height: 303px;
    border-radius: 24px; overflow: hidden;
    border: 1px solid var(--card-border);
    box-shadow: 0 10px 28px var(--card-shadow);
  }

  /* Front */
  .card--front { background: var(--card-white); }
  .brand {
    position: absolute; left: 26px; top: 36px;
    display: flex; align-items: center; gap: 12px;
  }
  .brand__dot {
    width: 46px; height: 46px; border-radius: 50%;
    background: var(--accent-yellow);
  }
  .brand__name {
    font-size: 25px; font-weight: 500; color: var(--ink-soft);
    line-height: 1.05;
  }
  .person {
    position: absolute; right: 26px; top: 26px; text-align: right;
  }
  .person__name { font-size: 17px; font-weight: 500; color: var(--ink); }
  .person__title { font-size: 11px; color: var(--ink); margin-top: 3px; margin-right: 34px; }

  .tagline-band {
    position: absolute; left: 0; right: 0; top: 122px; height: 17px;
    background: var(--band);
    display: flex; align-items: center; justify-content: center;
  }
  .tagline {
    font-size: 11px; font-weight: 500; letter-spacing: 0.62em;
    text-transform: uppercase; color: var(--band-text);
  }
  .email {
    position: absolute; left: 24px; top: 148px;
    font-size: 12px; color: var(--ink);
    display: flex; align-items: center; gap: 5px;
  }
  .offices {
    position: absolute; left: 24px; right: 20px; top: 180px;
    display: flex; gap: 58px;
  }
  .office { font-size: 12px; color: var(--ink); line-height: 1.45; }
  .office--satellite { font-size: 12.5px; margin-top: 12px; }
  .office__line { display: flex; align-items: flex-start; gap: 5px; }
  .office__line .indent { padding-left: 17px; }
  .icon { width: 12px; height: 12px; flex: none; margin-top: 2px; fill: var(--accent-yellow); }

  /* Back: light, open surface for handwritten notes */
  .card--back { background: var(--card-back); }
  .website {
    position: absolute; left: 0; right: 0; bottom: 24px; text-align: center;
    font-size: 13px; letter-spacing: 0.42em; color: var(--web-grey);
  }
</style>
</head>
<body>
<main class="stage">

  <section class="card card--front" aria-label="Card front">
    <div class="brand">
      <span class="brand__dot"></span>
      <span class="brand__name">Quambel<br>Systems, Inc.</span>
    </div>

    <div class="person">
      <p class="person__name">Delia Marchetti</p>
      <p class="person__title">CEO</p>
    </div>

    <div class="tagline-band"><span class="tagline">Design, Develop, Deploy</span></div>

    <p class="email">
      <svg class="icon" viewBox="0 0 12 12" aria-hidden="true"><path d="M0 2h12v8H0z M1 3l5 3.5L11 3v-.2H1z" fill-rule="evenodd"/></svg>
      dmarchetti@quambelsystems.example
    </p>

    <div class="offices">
      <div class="office office--hq">
        <p class="office__line">
          <svg class="icon" viewBox="0 0 12 12" aria-hidden="true"><path d="M6 0.5L0 6h1.7v5.5h3V8h2.6v3.5h3V6H12z"/></svg>
          <span>87 Corliss Avenue, #2260</span>
        </p>
        <p class="office__line"><span class="indent">Atlanta, GA 30301</span></p>
        <p class="office__line">
          <svg class="icon" viewBox="0 0 12 12" aria-hidden="true"><path d="M2.4 0.5l2 2.4-1.2 1.4c.8 1.7 2.1 3 3.8 3.8l1.4-1.2 2.4 2-1.4 2.4C4.8 11 1 7.2.3 2z"/></svg>
          <span>Office: 404.555.0178</span>
        </p>
        <p class="office__line">
          <svg class="icon" viewBox="0 0 12 12" aria-hidden="true"><path d="M3 0h5l1 1v3h2v8H1V4h2z M4 1v3h4V1.5z M3 6h6v1H3z M3 8h6v1H3z" fill-rule="evenodd"/></svg>
          <span>Fax: 404.555.0143</span>
        </p>
      </div>

      <div class="office office--satellite">
        <p class="office__line">
          <svg class="icon" viewBox="0 0 12 12" aria-hidden="true"><path d="M6 0.5L0 6h1.7v5.5h3V8h2.6v3.5h3V6H12z"/></svg>
          <span>315 West Harrow Lane Street</span>
        </p>
        <p class="office__line"><span class="indent">Suite 720 Savannah, GA 31401</span></p>
        <p class="office__line">
          <svg class="icon" viewBox="0 0 12 12" aria-hidden="true"><path d="M2.4 0.5l2 2.4-1.2 1.4c.8 1.7 2.1 3 3.8 3.8l1.4-1.2 2.4 2-1.4 2.4C4.8 11 1 7.2.3 2z"/></svg>
          <span>Office: 912.555.0162</span>
        </p>
        <p class="office__line">
          <svg class="icon" viewBox="0 0 12 12" aria-hidden="true"><path d="M3 0h5l1 1v3h2v8H1V4h2z M4 1v3h4V1.5z M3 6h6v1H3z M3 8h6v1H3z" fill-rule="evenodd"/></svg>
          <span>Fax: 404.555.0143</span>
        </p>
      </div>
    </div>
  </section>

  <section class="card card--back" aria-label="Card back, open space for notes">
    <p class="website">www.quambelsystems.example</p>
  </section>

</main>
</body>
</html>
```